Kolbrin new startup tech website refresh

We need a new website design for a tech startup company. We want a cutting edge high tech looking website. See kolbrin-example.com for the current site that needs to be updated with a fresh look. Use the info from the website.
We want the site to feel fast, sleek, and tech-driven while still speaking directly to the customers who will use Kolbrin. The design should highlight speed, efficiency, and precision with a monospace code font for headlines, stats, and technical details, paired with a clean sans-serif for body copy. This reinforces the product’s engineering credibility while keeping content easy to read.

Target Market(s)

tech Enterprises, Start up companies and Cloud providers

Industry/Entity Type

Tech

Number of Pages Required

2 page

Requirements
Must have
• We want the site to feel fast, sleek, and tech-driven while still speaking directly to the customers who will use Kolbrin. The design should highlight speed, efficiency, and precision with a monospace code font for headlines, stats, and technical details, paired with a clean sans-serif for body copy. This reinforces the product’s engineering credibility while keeping content easy to read.

```html
<!DOCTYPE html>
<html lang="en">
<head>
<meta charset="utf-8">
<title>Kolbrin – Run AI-built apps at C-speed</title>
<link href="https://fonts.googleapis.com/css2?family=Audiowide&family=Open+Sans:wght@400;600;700&display=swap" rel="stylesheet">
<style>
:root{
  --navy:#2e2a78;
  --navy-deep:#232060;
  --green:#5ee3a1;
  --gray-band:#efefef;
  --text:#555;
  --white:#fff;
  --circle:#ececec;
}
*{box-sizing:border-box;margin:0;padding:0}
html,body{width:1200px;height:3844px;overflow:hidden;background:var(--white)}
body{font-family:"Open Sans",Arial,sans-serif;color:var(--text);font-size:13px;line-height:1.38;position:relative}
.sec{position:absolute;left:0;width:1200px}
.center{text-align:center}
h2{font-family:"Audiowide",monospace,sans-serif;font-weight:400;color:var(--navy);font-size:32px;text-align:center;line-height:1.1}
.para{width:810px;margin:0 auto;text-align:center}
.para b{color:var(--navy)}

/* hero */
.hero{top:0;height:394px;background:linear-gradient(180deg,#0b1f3a 0%,#0f3553 45%,#0b2240 100%);color:var(--white);text-align:center}
.hero .logo{font-family:"Audiowide",monospace,sans-serif;font-size:48px;color:var(--green);padding-top:38px;line-height:1}
.hero h1{font-family:"Audiowide",monospace,sans-serif;font-weight:400;font-size:33px;color:var(--green);line-height:1.1;margin-top:20px}
.hero .lead{font-size:17px;line-height:1.35;margin-top:20px}
.hero .stats{font-size:14px;margin-top:18px}
.hero .btns{display:flex;justify-content:center;gap:34px;margin-top:24px}
.btn{width:142px;height:37px;border-radius:20px;border:2px solid var(--green);font-weight:700;font-size:14px;line-height:33px;color:var(--green)}
.btn.solid{background:var(--green);color:var(--navy)}

/* why */
.why{top:428px}
.why .para{margin-top:16px}
.pill{display:block;width:294px;height:38px;margin:22px auto 0;border:2px solid var(--navy);border-radius:20px;font-weight:700;color:var(--navy);line-height:34px;text-align:center;font-size:14px}
.cards{position:absolute;top:616px;left:194px;width:806px;display:flex;justify-content:space-between}
.card{width:380px;height:180px;background:var(--navy);border-radius:28px 28px 28px 0;box-shadow:-8px 8px 0 var(--green);color:var(--white);text-align:center;padding-top:26px;font-size:13px}
.card .ttl{font-family:"Audiowide",monospace,sans-serif;color:var(--green);font-size:30px;line-height:1.05;margin-bottom:18px}
.card ul{list-style:none}
.card li::before{content:"•  "}

/* icon rows */
.approach{top:834px}
.approach .sub{text-align:center;margin-top:14px}
.iconrow{position:absolute;left:0;width:1200px;display:flex;justify-content:center;gap:30px}
.item{width:180px;text-align:center}
.icon{width:150px;height:150px;margin:0 auto 24px;border-radius:50% 50% 18px 18px;background:linear-gradient(160deg,var(--green),#3fc98a 60%,var(--navy))}
.item .lbl{color:var(--navy);font-weight:700}

/* architecture */
.arch{top:1197px;height:191px;background:var(--gray-band);border-bottom:9px solid var(--green);padding-top:26px}
.cols{display:flex;justify-content:center;margin-top:22px}
.col{width:208px;text-align:center;padding:0 14px;border-right:1px solid #c8c8c8}
.col:last-child{border-right:0}
.col b{color:var(--navy)}

/* features */
.ai{top:1430px}
.ai .para{margin-top:14px}
.features{position:absolute;top:1721px;left:194px;width:806px;display:flex;justify-content:space-between}
.feat{width:154px;height:101px;background:var(--navy);color:var(--white);border-radius:14px 14px 14px 0;box-shadow:-6px 6px 0 var(--green);text-align:center;padding:12px 10px;font-size:13px}

/* gray consider */
.consider{top:2212px;height:221px;background:var(--gray-band);border-bottom:9px solid var(--green);padding-top:28px}
.consider .cols{margin-top:16px}
.consider .col{width:284px;text-align:left;padding:0 26px}
.consider .col::before{content:"•  "}
.consider .para{margin-top:12px}

/* roadmap */
.roadmap{position:absolute;top:3060px;left:194px}
.rm-text{font-family:"Open Sans",Arial,sans-serif;fill:var(--navy);text-anchor:middle}
.step{font-family:"Open Sans",Arial,sans-serif;fill:var(--white);text-anchor:middle;font-weight:700}

/* team */
.team{top:3360px}
.team-row{display:flex;justify-content:center;gap:72px;margin-top:18px}
.member{width:200px;text-align:center}
.member b{color:var(--navy)}

/* footer */
.footer{top:3588px;height:256px;background:var(--navy);border-bottom:14px solid var(--green);text-align:center;color:var(--white);padding-top:30px}
.footer .logo{font-family:"Audiowide",monospace,sans-serif;font-size:46px;color:var(--green);line-height:1}
.footer .cu{font-family:"Audiowide",monospace,sans-serif;font-size:30px;color:var(--green);margin-top:8px}
.footer .k{color:var(--green);font-weight:700;margin-top:14px}
.footer .v{font-size:14px}
</style>
</head>
<body>

<header class="sec hero">
  <div class="logo">Kolbrin</div>
  <h1>Run AI-built apps at C-speed,<br>with no runtime overhead</h1>
  <p class="lead">Kolbrin gives AI a fast, local runtime to compile to.<br>Your app logic stays high-level, runs like hand-written C,<br>and costs a fraction to operate.</p>
  <p class="stats">104 KB actors | 300,000 invocations/sec per core | Zero cold-starts</p>
  <div class="btns"><span class="btn solid">The Deck</span><span class="btn">The Code</span><span class="btn">Contact</span></div>
</header>

<section class="sec why">
  <h2>Why Kolbrin?</h2>
  <p class="para">The serverless paradigm has unlocked horizontal scale but sacrificed vertical scale. Kolbrin addresses this by inventing zero-overhead abstractions that enable rapid development with high-level interfaces for server and service authoring, while delivering performance that meets or exceeds state-of-the-art specialized servers.</p>
  <span class="pill">See our deck for a deeper summary</span>
</section>

<div class="cards">
  <div class="card"><div class="ttl">Current<br>Platforms</div>
    <ul><li>Heavy cold starts (10–100ms)</li><li>High per-invocation overhead</li><li>Stateless, hash-partitioned scaling</li></ul></div>
  <div class="card"><div class="ttl" style="font-size:40px;margin-bottom:20px">Kolbrin</div>
    <ul><li>Instant actor dispatch (µs – single page fault)</li><li>8KB memory per actor + 96 KB per socket (tunable)</li><li>Ontological locality for state persistence</li></ul></div>
</div>

<section class="sec approach">
  <h2>Our Approach</h2>
  <p class="sub">krvex is a C service stack composed of four frameworks:</p>
</section>
<div class="iconrow" style="top:910px">
  <div class="item"><div class="icon" role="img" aria-label="Cloud with gear icon"></div><span class="lbl">Cloud Function framework:</span><br>A cloud and edge application server and runtime library (FrostRT).</div>
  <div class="item"><div class="icon" role="img" aria-label="Service cycle with gear icon"></div><span class="lbl">Service framework:</span><br>A “Super-Server” protocol suite built on listening and accepted micro-processes.</div>
  <div class="item"><div class="icon" role="img" aria-label="Gear with folder icon"></div><span class="lbl">Actor framework:</span><br>A soft-real-time micro-kernel that drives micro-processes with coroutines.</div>
  <div class="item"><div class="icon" role="img" aria-label="Code gear with connections icon"></div><span class="lbl">Threading framework:</span><br>An event-based, stackless coroutine system with message-passing and I/O aggregation.</div>
</div>

<section class="sec arch">
  <h2>The architecture comprises:</h2>
  <div class="cols">
    <div class="col"><b>Threading:</b><br>Novel M:1 micro-process coroutine library.</div>
    <div class="col"><b>Actor:</b><br>Deductive poller micro-kernel operating across isolated huge-page micro-heaps.</div>
    <div class="col"><b>Service:</b><br>Virtual forking-server built on micro-processes.</div>
    <div class="col"><b>Cloud Function:</b><br>FrostRT framework maintaining state in micro-processes.</div>
  </div>
</section>

<section class="sec ai">
  <h2>AI-Powered Development</h2>
  <p class="para">Today’s AI startups promise no-code app building—but they struggle with platform code, because platforms manage resources in space and time, which requires spatial reasoning—something AI still handles poorly. As a result, AI-generated apps default to high-level platforms (e.g., serverless, managed runtimes), which are easy for AI to target but deliver unhappy trade-offs: bloated runtime overhead, poor performance, and skyrocketing costs at scale. Kolbrin flips that script. We expose familiar, high-level interfaces (the ones people use in expensive managed runtimes) on a lean, low-level platform built from the ground up for efficiency. Then we let AI translate “slow” platform calls into our fast, resource-local primitives. In other words, we turn a problem AI is bad at (writing low-level platform code) into one it’s actually good at (translating from one API to another). The result: AI-assisted app development that runs like hand-optimized C—without the C-level complexity.</p>
  <h2 style="margin-top:28px">Key Features</h2>
</section>
<div class="features">
  <div class="feat">Single huge-page fault loads the entire micro-process on each I/O dispatch</div>
  <div class="feat">Persistent, memory-protected mappings backed by huge pages</div>
  <div class="feat">104 KB footprint per actor (8 KB process + 96 KB tunable ring buffers)</div>
  <div class="feat">Cooperative and isolated scheduling</div>
  <div class="feat">Language-agnostic bindings<br>(C, JavaScript, etc.)</div>
</div>

<section class="sec" style="top:1860px">
  <h2>Performance</h2>
  <p class="para" style="margin-top:14px">Benchmarks demonstrate over 300,000 full HTTP requests per second per core on a commodity i7,<br>with consistent sub-millisecond median latency and deterministic memory usage.</p>
  <h2 style="margin-top:34px">Ontological Objects and Locality of Reference</h2>
  <p class="para" style="margin-top:12px">We invented <b>the locality method of ontological objects</b>, a novel paradigm complementing lambda calculus. All framework levels are cache-aware and designed to leverage modern virtual memory and processor capabilities. While unrestricted C is supported, selective, cache-aware encapsulation enables extreme performance.</p>
  <p class="para" style="margin-top:16px">Zero-overhead abstractions deliver high-level threaded I/O and OTP-style actor interfaces with exceptional performance. At their core, krvex coroutine continuations are three times faster than Go goroutines, and throughput further improves due to application code locality, unencumbered by Go’s work-stealing scheduler or garbage collection. <b>Smaller cache sizes amplify krvex’s performance advantage</b> because it explicitly optimizes for spatial limits.</p>
</section>

<section class="sec consider">
  <h2>Consider the following:</h2>
  <div class="cols">
    <div class="col">Library data co-locates within the same huge-page micro-process</div>
    <div class="col">The compiler can leverage lambda calculus when low-level calls do not escape</div>
    <div class="col">Link-time optimization (LTO) applies across libraries, enhancing static locality beyond typical single-binary builds in Go and Rust</div>
  </div>
  <p class="para">The <b>unexpected benefit of ontological objects is improved lambda calculus:</b> functional paradigms ease object management, while <b>ontological objects enable more effective function optimization</b>.</p>
</section>

<section class="sec" style="top:2468px">
  <h2>krvex Virtual Sockets</h2>
  <p class="para" style="margin-top:18px">In krvex, virtual sockets (vk_vectoring) use bidirectional tx/rx iovec ring buffers with automatic wrapping. They integrate directly with scheduling and network polling, avoiding low-water marks and complex flushing logic. Deductive polling occurs with automatic registration and flushing at optimal points, <b>eliminating unnecessary copies and syscalls</b>.</p>
  <p class="para" style="margin-top:16px">Despite being lower-level, these I/O interfaces are higher-level than standard streams—even Python file objects—enabling easy development of state-of-the-art socket-based servers. krvex is <b>a server authoring toolkit</b> in the similar way EmbedDB is a database authoring toolkit. In fact, the embedded nature of EmbedDB mates with the locality paradigm of krvex.</p>
  <h2 style="margin-top:30px">Use Cases</h2>
</section>
<div class="iconrow" style="top:2739px">
  <div class="item"><div class="icon" role="img" aria-label="Cloud with gear icon"></div><span class="lbl">Cloud Function Framework</span><br>Build and deploy full cloud &amp; edge applications with a C FrostRT cloud function interface providing isolated yet unbounded compute.</div>
  <div class="item"><div class="icon" role="img" aria-label="Service cycle with gear icon"></div><span class="lbl">Service framework</span><br>Build data services with custom protocols using the Super-Server interface.</div>
  <div class="item"><div class="icon" role="img" aria-label="Gear with folder icon"></div><span class="lbl">Actor framework</span><br>Execute soft-real-time actors for Edge AI and event-driven tasks with &lt;2 ms latency.</div>
  <div class="item"><div class="icon" role="img" aria-label="Code gear with connections icon"></div><span class="lbl">Threading framework</span><br>Power deterministic, high-throughput coroutines (300K invocations/sec) with message-passing I/O aggregation.</div>
</div>

<h2 class="sec" style="top:3018px">Roadmap</h2>
<svg class="roadmap" width="810" height="313" viewBox="0 0 810 313">
  <path d="M2 164 A152 152 0 0 0 306 164 L254 164 A100 100 0 0 1 54 164 Z" fill="var(--navy)"/>
  <path d="M254 164 A152 152 0 0 1 558 164 L506 164 A100 100 0 0 0 306 164 Z" fill="var(--green)"/>
  <path d="M503 164 A152 152 0 0 0 807 164 L755 164 A100 100 0 0 1 555 164 Z" fill="var(--navy)"/>
  <circle cx="154" cy="164" r="100" fill="var(--circle)"/>
  <circle cx="406" cy="164" r="100" fill="var(--circle)"/>
  <circle cx="655" cy="164" r="100" fill="var(--circle)"/>
  <text class="step" x="154" y="287" font-size="8">STEP</text><text class="step" x="154" y="307" font-size="20">01</text>
  <text class="step" x="406" y="14" font-size="8">STEP</text><text class="step" x="406" y="34" font-size="20">02</text>
  <text class="step" x="655" y="287" font-size="8">STEP</text><text class="step" x="655" y="307" font-size="20">03</text>
  <text class="rm-text" x="154" y="150" font-size="22" font-weight="700">Q3 2025:</text>
  <text class="rm-text" x="154" y="178" font-size="22">Public</text>
  <text class="rm-text" x="154" y="205" font-size="22">Beta Launch</text>
  <text class="rm-text" x="406" y="150" font-size="22" font-weight="700">Q4 2025:</text>
  <text class="rm-text" x="406" y="178" font-size="22">CLI &amp; SDK</text>
  <text class="rm-text" x="406" y="205" font-size="22">Release</text>
  <text class="rm-text" x="655" y="150" font-size="22" font-weight="700">Q1 2026:</text>
  <text class="rm-text" x="655" y="178" font-size="22">Managed Cloud</text>
  <text class="rm-text" x="655" y="205" font-size="22">Service</text>
</svg>

<section class="sec team">
  <h2>Team</h2>
  <div class="team-row">
    <div class="member"><b>Rowan Ellery</b><br>Platform Development, a generalist with deep experience across all levels, from web front-ends to operating system internals. Decades of marketing technology experience.</div>
    <div class="member"><b>Milo Varga</b><br>Application Development, a prolific application developer who can build novel products on any platform. Decades of government contracting experience.</div>
    <div class="member"><b>Dana Prewitt</b><br>Business Development, the king of customer loyalty. Decades operating multiple businesse</div>
  </div>
</section>

<footer class="sec footer">
  <div class="logo">Kolbrin</div>
  <div class="cu">Contact Us</div>
  <div class="k">Email</div>
  <div class="v">info@kolbrin-example.com</div>
  <div class="k">ProNet</div>
  <div class="v">Kolbrin ProNet Page</div>
</footer>

</body>
</html>
```